Emergency Vehicle Installer and Security Firm Needs a Business Card

Our company "Corvalt" need a business card for our Emergency Vehicle Equipment Installation and Infrastructure Security Business. We are contract designers, manufacturers and installers for Emergency Vehicle Fleets. This includes installation of Emergency Lights, Sirens, Vehicle Graphics and Radio Communications. We also supply this products to an international market. We also do consultant, and installation of high level security access, alarm and surveillance equipment for medium to large size businesses.

The design should represent a level of trust in our professionalism and expertise. It should visually display our ongoing relationship with the emergency services, but not overtake our commitment to high level security options.

Target Market(s)

Emergency Services and Businesses requiring high level security

Industry/Entity Type

Business

Contact Information for Business Card

*note complete details will be given to the winning designer for revising. The name "Mark Pell will be used to fill in name".

Mark Pell
Managing Director
Corvalt NZ Limited
Phone: +64 027 604 91352
Email: mark.pell@corvalt-example.co.nz

Requirements
Must have
• Card must be in black. Using our logo on the top as supplied. Designers should try having the reverse side as a blurred image of police lights (red and blue) with our logo in greyscale in the centre (this is not particularly a requirement, but feel free to play around with this option).
Nice to have
• A card design that looks good when spot UV printed. A clean compact and graphic design. A grey scale feel on the front (excluding logo, but you can play around with that idea). Rounded smooth text.
Should not have
• Will update this section as designs come through - feel free to submit what you feel would look good.

```html
<!DOCTYPE html>
<html lang="en">
<head>
<meta charset="utf-8">
<title>Corvalt Business Card</title>
<link rel="stylesheet" href="https://fonts.googleapis.com/css2?family=Arimo:wght@400;700&display=swap">
<style>
  :root {
    --page: #ecebe7;
    --card-black: #1e1a1a;
    --card-grey: #a9a9a9;
    --accent-red: #e2231a;
    --text-dark: #1e1a1a;
    --text-light: #c9c9c9;
    --brand-grey: #b5b5b5;
  }
  * { margin: 0; padding: 0; box-sizing: border-box; }
  html, body {
    width: 1200px;
    height: 1200px;
    overflow: hidden;
    background: var(--page);
    font-family: "Arimo", Arial, sans-serif;
  }
  .canvas {
    position: relative;
    width: 1200px;
    height: 1200px;
  }
  .card {
    position: absolute;
    width: 760px;
    height: 434px;
    overflow: hidden;
    box-shadow: 0 6px 18px rgba(0,0,0,0.25);
  }
  .card-front { left: 110px; top: 110px; }
  .card-back  { left: 330px; top: 650px; background: var(--card-black); }

  .front-art { position: absolute; inset: 0; width: 100%; height: 100%; }

  .person {
    position: absolute;
    right: 70px;
    top: 92px;
    text-align: right;
  }
  .person-name {
    color: var(--accent-red);
    font-size: 34px;
    font-weight: 400;
  }
  .person-role {
    color: var(--text-light);
    font-size: 17px;
    margin-top: 6px;
  }

  .company {
    position: absolute;
    left: 86px;
    top: 285px;
  }
  .company-name {
    color: var(--accent-red);
    font-size: 34px;
    font-weight: 400;
    margin-bottom: 14px;
  }
  .contact-line {
    display: flex;
    align-items: center;
    gap: 10px;
    color: var(--text-dark);
    font-size: 19px;
    line-height: 30px;
  }
  .contact-icon { width: 16px; height: 16px; flex: none; }

  .brand {
    position: absolute;
    inset: 0;
    display: flex;
    align-items: center;
    justify-content: center;
  }
  .brand-name {
    color: var(--brand-grey);
    font-size: 72px;
    font-weight: 700;
    letter-spacing: 2px;
    line-height: 1;
    margin-top: 20px;
  }
</style>
</head>
<body>
<main class="canvas">

  <section class="card card-front" aria-label="Business card front">
    <svg class="front-art" viewBox="0 0 760 434" preserveAspectRatio="none" aria-hidden="true">
      <rect width="760" height="434" fill="var(--card-grey)"/>
      <path d="M330,0 C255,90 270,165 395,230 C505,290 515,365 515,434 L760,434 L760,0 Z"
            fill="var(--card-black)"/>
      <path d="M330,0 C255,90 270,165 395,230 C505,290 515,365 515,434"
            fill="none" stroke="var(--accent-red)" stroke-width="14"/>
    </svg>

    <div class="person">
      <div class="person-name">Mark Pell</div>
      <div class="person-role">Managing Director</div>
    </div>

    <div class="company">
      <div class="company-name">Corvalt NZ Limited</div>
      <div class="contact-line">
        <svg class="contact-icon" viewBox="0 0 16 16" aria-hidden="true">
          <circle cx="8" cy="8" r="7" fill="none" stroke="var(--accent-red)" stroke-width="1.4"/>
          <path d="M5.5,4.5 l1.3,-0.3 l0.8,1.8 l-0.9,0.7 a5,5 0 0 0 2.6,2.6 l0.7,-0.9 l1.8,0.8 l-0.3,1.3 a6,6 0 0 1 -6,-6 z" fill="var(--accent-red)"/>
        </svg>
        <span>+64 027 604 91352</span>
      </div>
      <div class="contact-line">
        <svg class="contact-icon" viewBox="0 0 16 16" aria-hidden="true">
          <rect x="1" y="3.5" width="14" height="9" fill="none" stroke="var(--accent-red)" stroke-width="1.4"/>
          <path d="M1,3.5 L8,9 L15,3.5" fill="none" stroke="var(--accent-red)" stroke-width="1.4"/>
        </svg>
        <span>mark.pell@corvalt-example.co.nz</span>
      </div>
    </div>
  </section>

  <section class="card card-back" aria-label="Business card back">
    <div class="brand">
      <div class="brand-name">CORVALT</div>
    </div>
  </section>

</main>
</body>
</html>
```